Lunar Ledger - Minimalistic Single Page Web Design

Project: We are in the process of creating a new Corp Identity. Design a website for our company incorporating the Logo recently designed and selected from a SketchHive contest. (attached)

Designers: For this project, you need to design a minimalistic single page, modern website. Beside text and image placement, you will also need to describe user interface, how content is presented and so on.
- Design Layout
- Design Image placements (if any)
- Design menu and buttons
- Design menu and buttons placements
- Design content layout
- Design overall effect and feel of website
- Design color scheme
- Design content style (tone and style of content, words type, how much)
- Design user interface (how do you scroll, what happens when you mouseover buttons, where do certain links and buttons lead you)

Coding Requirements: You need to design the website with a modern perspective on website visuals and effects. Jquery, HTML5 (no FLASH please). You do not need to code for this particular contest, but if you can also code, great, tell me and let me know how I can hire you to complete it. If you know someone that can code your vision, great, let me know. If not, you need to be clear and concise, and be willing to help me communicate with a developer to get the site executed. The web site needs to be modern and dynamic.

Company Name:
Lunar Ledger; Lunar-Ledger; LunarLedger

Domain: www.lunar-ledger.example

Company Industry:
Lunar Ledger provides consulting in areas of finance, accounting, business organization, and set up.
- Bookkeeping
- Project Management
- Budget Management
- Cash Management
- Receipt Management
- Filing and Records Management
- Training of administration and accounting staff
- Financial Reports
- Spreadsheets
- Graphs, charts and trend analysis
- Business set up
- Tax filings
- Payroll and HR

Clients:
- Small to medium size businesses
- Proprietors
- Entrepreneurs
- Mom & Pops Shops
- We cater to every industry

Corporate Identity:
- Past: I have never complete a webpage for my company. I did scratch several projects that were started and never completed. I fell in love with stick figures, whimsical designs, similar to that of "Cratebin", I believed in simplicity and minimalism. However, I was not effective in find the right people to complete my project. Bits and pieces of the website was designed, but never executed.

- Current: I need a webpage design. The web design must align with the current logo aesthetics.The current logo is new. I selected this logo for its simplicity and modern feel. It also incorporated an image of a trending graph, which fits with my company's profile. Still, I am leaning towards simple design, minimalism with boldness. I like my new webpage to be mature and professional, but I want it to portray energy and youth. So no "traditional corp" like design. I like new HTML5 elements, jquery and fun and beautiful forms and buttons. Less image is more.

Note: Please improvise according to your taste and professional perspective, you do not have to follow my suggestions word for word.

Features & Layout:
- Single page layout
- Vertical scroll
- Framed sections so that it looks good on the screen
- Well designed and strategically placed menu bar
- Fills a modern browser
- Beautiful color scheme that pops
- Incorporate Logo aesthetics

Fonts and Type:
- This is an element of the overall design
- I love clean fonts
- Fonts that adds meaning to the overall effect
- Clean

Sounds
- Please no cheesy sounds and background music

Images:
- To your liking
- But please, no lame corp people in suits
- No lame photographs
- I like stick figures
- I like whimsical illustrations

Landing Page:
- This should be the bulk of your design
- The landing page must be impressive, eye catchy
- Bold

Menu Bar:
- Header (introduction and landing page)
- Service & Products
- Company (about us)
- Affiliates and Clients (reference area)
- Contact (contact us area)
- Footer

Colors:
- Up to you, I just like things clean and easy to read
- No black background behind text
- Incorporate Logo Colors

Web Effects:
- According to your liking
- You will need to be involve to communicate the layout and design to the developer, so you need to be clear in your design.

Content:
- You personally don't have to come up with the content, but if you can great.
- I will help come up with the content throughout the contect timeframe, just let me know what you want
- I do not like too much content in my website. The most for each section is 2-3 lines if any.
- Combination could also be one liners.
- I like minimalistic approach.
- If you are not creating the final content, you need to show what type of content need to be created and in what style or tone.

Samples and Inspirations:
- http://scrollkin.example/
- http://zentrovo.example/#top
- http://brightmopservices.example/#about
- http://pixelgazette.example/inspiration/23-inspiring-single-page-designs
- http://www.tobiaskernstudio.example/
- http://www.ravelquist.example/

This I do not want:
- Too much popups (none if possible)
- Images of people
- Images of people in suits
- Stereotypical images of accountants
- Scrolling marquee
- Clip arts
Updates

Designers, I want to stress the fact that I am looking for a design, not simply a website. The website is 1 page long. Text and content should be minimal. So this means that the design has to do most of the talking. Please do not submit template like web designs, I can pull this off myself if needed. I need you to design a great header, footer and the connecting tissue from landing to end of the page. The entire design needs to flow.

Again, please do not use images of corp people or anything like that. Please think outside the box in how you want to express the company.

Some ideas:
An illustration from beginning to end of the website, have a story.
Add colors to the back ground. 
The background should not get in the way of reading the text, but it does not have to be boring.
Be bold in your design.

Also, please describe more about your design when you submit. Please don't submit a template like design and have no explanation for your actions.

Also, fee free to ask me questions. I am here to help. I check this everyday, so please contact if you need anything.

Designers, please read the details of my post before you submit the design.

If you have a great concept idea but is worry, you can go ahead and submit a pencil draft and ask my opinion before you work anymore on it.

Please see the website samples below for what I am really looking for:

Reason: Hi everyone, I am extending the deadline. It looks like some design are still pending completion, and I want you to have enough time to work on it.

Industry/Entity Type

Accounting

```html
<!DOCTYPE html>
<html lang="en">
<head>
<meta charset="utf-8">
<title>Lunar Ledger – Single Page</title>
<link rel="stylesheet" href="https://fonts.googleapis.com/css2?family=Alfa+Slab+One&family=Cabin:wght@400;500&family=Lobster&family=Quicksand:wght@500&display=swap">
<style>
  :root{
    --lime:#97d014;
    --lime-soft:#c9e98a;
    --lime-pale:#e9f7cc;
    --navy:#141e96;
    --navy-ink:#2a35a8;
    --lavender:#c9cdf3;
    --white:#ffffff;
    --stage:#000000;
  }
  *{margin:0;padding:0;box-sizing:border-box}
  html,body{width:786px;height:1200px;overflow:hidden;background:var(--stage)}
  .page{
    position:absolute;left:196.5px;top:0;width:450px;height:1374px;
    transform:scale(0.8734);transform-origin:0 0;
    background:var(--lime);overflow:hidden;
    font-family:"Cabin",sans-serif;
  }
  .backdrop{position:absolute;inset:0;width:450px;height:1374px}
  .topbar{position:absolute;left:0;top:0;width:450px;height:16px;background:var(--white)}
  .brand{position:absolute;left:45px;top:3px;font:500 8px "Quicksand",sans-serif;color:var(--navy);display:flex;align-items:center;gap:3px}
  .brand-dot{width:5px;height:5px;border-radius:50%;background:var(--lime)}
  .nav{position:absolute;left:216px;top:0;display:flex;list-style:none}
  .nav li{font:500 6px "Quicksand",sans-serif;color:var(--navy);width:45px;text-align:center;height:16px;line-height:16px}
  .nav li.is-active{color:var(--lime);border-bottom:1.5px solid var(--navy-ink)}
  .hero-art{position:absolute;left:50px;top:38px;width:122px;height:78px;border-radius:10px;
    background:radial-gradient(circle at 50% 45%,#f3d7a8 0 14%,#6fa6e8 15% 40%,rgba(255,255,255,.55) 41%,rgba(151,208,20,0) 70%)}
  .hero-mark{position:absolute;left:186px;top:22px;font:400 100px/1 "Alfa Slab One",serif;color:var(--navy)}
  .hero-title{position:absolute;left:248px;top:38px;font:400 18px/26px "Alfa Slab One",serif;letter-spacing:2px;color:var(--lime-pale);text-transform:uppercase}
  .trail{position:absolute;width:80px;border-radius:40px}
  .trail--upper{left:84px;top:128px;height:440px;
    background:linear-gradient(180deg,rgba(255,255,255,.16),rgba(255,255,255,.08) 60%,rgba(20,30,150,.12))}
  .trail--lower{left:84px;top:1045px;height:329px;
    background:linear-gradient(180deg,rgba(255,255,255,.10),rgba(255,255,255,.18))}
  .intro{position:absolute;left:196px;top:256px;width:200px;color:var(--lavender);font-size:11px;line-height:19px}
  .intro strong{font-weight:500;font-size:14px}
  .services-title{position:absolute;left:180px;top:488px;font:400 30px/42px "Alfa Slab One",serif;letter-spacing:3px;color:var(--navy-ink);text-transform:uppercase}
  .services{position:absolute;left:34px;top:580px;display:grid;grid-template-columns:repeat(4,95px);grid-auto-rows:116px;list-style:none}
  .service{display:flex;flex-direction:column;align-items:center}
  .service svg{width:70px;height:66px}
  .service-label{font:400 11.5px/15px "Lobster",cursive;color:var(--navy);text-align:center;margin-top:4px}
  .bulb-art{position:absolute;left:84px;top:938px;width:94px;height:100px;border-radius:50%;
    background:radial-gradient(circle at 50% 40%,#d8f08f 0 30%,rgba(151,208,20,.45) 55%,rgba(255,255,255,0) 72%)}
  .contact-title{position:absolute;left:185px;top:1094px;font:400 30px/40px "Alfa Slab One",serif;letter-spacing:2px;color:var(--lime-pale);text-transform:uppercase}
  .contact-form{position:absolute;left:187px;top:1145px;width:218px;display:flex;flex-direction:column}
  .field{width:218px;height:25px;border:0;background:var(--lime-soft);color:var(--white);font:400 15px "Cabin",sans-serif;padding:0 6px;margin-bottom:7px;outline:none;resize:none}
  .field::placeholder{color:var(--white)}
  .field--message{height:89px;padding-top:2px;margin-bottom:14px}
  .send{width:218px;height:24px;border:0;background:var(--white);color:var(--lime);font:400 14px "Alfa Slab One",serif;letter-spacing:2px}
</style>
</head>
<body>
<main class="page">
  <svg class="backdrop" viewBox="0 0 450 1374" aria-hidden="true">
    <path d="M0 1374V0h450v1374z" fill="#97d014"/>
    <path d="M0 170C40 155 80 130 110 125C170 140 300 160 450 172V425C350 432 230 440 180 480C152 505 140 540 136 572C128 520 100 450 0 426Z" fill="#141e96"/>
    <path d="M0 426C100 450 128 520 136 572C140 540 152 505 180 480C230 440 350 432 450 425V1088C350 1070 230 1060 120 1040C80 1060 40 1075 0 1085Z" fill="#ffffff"/>
  </svg>

  <header class="topbar">
    <div class="brand"><span>Lunar Ledger</span><span class="brand-dot"></span></div>
    <ul class="nav">
      <li class="is-active">Home</li><li>About</li><li>Services</li><li>Contact</li>
    </ul>
  </header>

  <div class="hero-art" role="img" aria-label="Stick-figure consultant surrounded by small finance and communication icons"></div>
  <div class="hero-mark" aria-hidden="true">?</div>
  <h1 class="hero-title">Don't<br>know how<br>to decide</h1>

  <div class="trail trail--upper" role="img" aria-label="Dashed looping trail winding down from the hero to the services section"></div>

  <p class="intro">We provides consulting in<br>areas of <strong>finance, accounting,<br>business organization,</strong><br>and <strong>set up.</strong></p>

  <h2 class="services-title">What we<br>can do</h2>

  <svg width="0" height="0" style="position:absolute" aria-hidden="true">
    <symbol id="bubble" viewBox="0 0 70 66">
      <path d="M35 2C17 2 3 16 3 33S17 64 35 64c9 0 16-3 21-8l10 4-5-10c4-5 6-11 6-17C67 16 53 2 35 2Z" fill="#fff" stroke="#222" stroke-width="1.2"/>
    </symbol>
  </svg>

  <ul class="services">
    <li class="service"><svg viewBox="0 0 70 66"><use href="#bubble"/><rect x="24" y="21" width="22" height="26" fill="#141e96"/><path d="M37 21v12l3-3 3 3V21" fill="#fff"/><rect x="27" y="21" width="2" height="26" fill="#fff"/></svg><span class="service-label">Book<br>Keeping</span></li>
    <li class="service"><svg viewBox="0 0 70 66"><use href="#bubble"/><circle cx="35" cy="33" r="13" fill="#141e96"/><path d="M35 25v9h7" stroke="#fff" stroke-width="2.4" fill="none"/></svg><span class="service-label">Project<br>Management</span></li>
    <li class="service"><svg viewBox="0 0 70 66"><use href="#bubble"/><path d="M21 38l9-9 6 5 10-10" stroke="#141e96" stroke-width="3" fill="none"/><path d="M42 22h7v7z" fill="#141e96"/><rect x="19" y="42" width="32" height="2.5" fill="#141e96"/></svg><span class="service-label">Budget<br>Management</span></li>
    <li class="service"><svg viewBox="0 0 70 66"><use href="#bubble"/><circle cx="35" cy="33" r="13" fill="#141e96"/><text x="35" y="39" font-family="Cabin,sans-serif" font-size="16" fill="#fff" text-anchor="middle">$</text></svg><span class="service-label">Cash<br>Management</span></li>

    <li class="service"><svg viewBox="0 0 70 66"><use href="#bubble"/><path d="M25 20h14l7 7v20H25z" fill="none" stroke="#141e96" stroke-width="2.4"/><path d="M29 32h12M29 37h12M29 42h8" stroke="#141e96" stroke-width="2"/></svg><span class="service-label">Receipt<br>Management</span></li>
    <li class="service"><svg viewBox="0 0 70 66"><use href="#bubble"/><g fill="#141e96"><rect x="22" y="24" width="4" height="4"/><rect x="22" y="31" width="4" height="4"/><rect x="22" y="38" width="4" height="4"/><rect x="29" y="24" width="19" height="4"/><rect x="29" y="31" width="19" height="4"/><rect x="29" y="38" width="19" height="4"/></g></svg><span class="service-label">Filling &amp; Record<br>Management</span></li>
    <li class="service"><svg viewBox="0 0 70 66"><use href="#bubble"/><path d="M29 34l-5 13 5-2 3 4 3-10M41 34l5 13-5-2-3 4-3-10" fill="#141e96"/><circle cx="35" cy="28" r="9" fill="none" stroke="#141e96" stroke-width="3"/></svg><span class="service-label">Training of<br>Administration</span></li>
    <li class="service"><svg viewBox="0 0 70 66"><use href="#bubble"/><g fill="#141e96"><rect x="25" y="32" width="5" height="12"/><rect x="32" y="22" width="5" height="22"/><rect x="39" y="28" width="5" height="16"/><rect x="22" y="45" width="26" height="2"/></g></svg><span class="service-label">Financial<br>Reports</span></li>

    <li class="service"><svg viewBox="0 0 70 66"><use href="#bubble"/><path d="M27 20h11l6 6v21H27z" fill="none" stroke="#141e96" stroke-width="2.6"/></svg><span class="service-label">Spreadsheets</span></li>
    <li class="service"><svg viewBox="0 0 70 66"><use href="#bubble"/><g fill="#141e96"><rect x="24" y="34" width="6" height="11"/><rect x="32" y="28" width="6" height="17"/><rect x="40" y="20" width="6" height="25"/></g></svg><span class="service-label">Graph, Chart<br>&amp; Analysis</span></li>
    <li class="service"><svg viewBox="0 0 70 66"><use href="#bubble"/><path d="M35 19l12 4v9c0 8-6 13-12 16-6-3-12-8-12-16v-9z" fill="#141e96"/><text x="35" y="38" font-family="Cabin,sans-serif" font-size="12" fill="#fff" text-anchor="middle">$</text></svg><span class="service-label">Tax<br>Fillings</span></li>
    <li class="service"><svg viewBox="0 0 70 66"><use href="#bubble"/><g fill="#141e96"><circle cx="35" cy="27" r="7"/><path d="M22 47c0-8 6-12 13-12s13 4 13 12z"/></g></svg><span class="service-label">Payroll<br>&amp; HR</span></li>
  </ul>

  <div class="bulb-art" role="img" aria-label="Hand-drawn light bulb with a sparkle of idea rays"></div>
  <div class="trail trail--lower" role="img" aria-label="Dashed looping trail continuing from the light bulb down the contact section"></div>

  <h2 class="contact-title">Contact</h2>
  <form class="contact-form">
    <input class="field" type="text" placeholder="Name">
    <input class="field" type="email" placeholder="E-mail">
    <textarea class="field field--message" placeholder="Message"></textarea>
    <button class="send" type="button">SEND</button>
  </form>
</main>
</body>
</html>
```